Podcast Graphics For Internet Business Building Podcast

We need new podcast graphics.
1400x1400
300dpi

Needs to include text "Quiet Harbor Ledger Hour" as the podcast title and "Creative Internet Income Strategies" as a subtitle.

We like blue and grey as our main colors, but are open to other schemes.

Please see attached image for an example of podcast graphics we like. While we prefer a more plain look, it would be nice to have a subtle hint related to a "machine" in the background. Something like a pencil sketch of cogs like on the Quiet Harbor Ledger 10 book cover (attached image).

Target Market(s)

online entrepreneurs or those who want to start an online business

Font styles to use
Sans Serif

Colors
0455a3
3277b5

Requirements
Must have
• Text noted in project description
Should not have
• No money symbols or flashy "make money" type things.

```html
<!DOCTYPE html>
<html lang="en">
<head>
<meta charset="utf-8">
<title>Quiet Harbor Ledger Hour – Podcast Cover</title>
<link rel="stylesheet" href="https://fonts.googleapis.com/css2?family=Roboto:wght@300&display=swap">
<style>
  :root {
    --blue-edge: #0270bd;
    --blue-mid: #0389d4;
    --blue-core: #09a2e6;
    --frame-line: #7fdaf8;
    --title-fill: #e6f5fd;
    --subtitle-fill: #e6f5fd;
    --subtitle-rule: #2fd0f2;
  }
  html, body {
    margin: 0;
    padding: 0;
    width: 1200px;
    height: 1200px;
    overflow: hidden;
    background: #ffffff;
  }
  .cover {
    display: block;
    width: 1200px;
    height: 1200px;
  }
  .podcast-title {
    font-family: "Roboto", "Helvetica Neue", sans-serif;
    font-weight: 300;
    font-size: 92px;
    letter-spacing: 2px;
    fill: var(--title-fill);
  }
  .subtitle {
    font-family: "Roboto", "Helvetica Neue", sans-serif;
    font-weight: 300;
    font-size: 53px;
    fill: var(--subtitle-fill);
  }
</style>
</head>
<body>
<svg class="cover" viewBox="0 0 1200 1200" xmlns="http://www.w3.org/2000/svg" role="img" aria-label="Quiet Harbor Ledger Hour – Creative Internet Income Strategies">
  <defs>
    <radialGradient id="backdrop-glow" cx="50%" cy="50%" r="62%">
      <stop offset="0" stop-color="var(--blue-core)"/>
      <stop offset="0.55" stop-color="var(--blue-mid)"/>
      <stop offset="1" stop-color="var(--blue-edge)"/>
    </radialGradient>
    <radialGradient id="floor-shadow" cx="50%" cy="50%" r="50%">
      <stop offset="0" stop-color="#03456f" stop-opacity="0.6"/>
      <stop offset="1" stop-color="#03456f" stop-opacity="0"/>
    </radialGradient>
  </defs>

  <rect class="backdrop" width="1200" height="1200" fill="url(#backdrop-glow)"/>

  <path class="inner-frame"
        d="M47 47 H1059 A94 94 0 0 1 1153 141 V1153 H141 A94 94 0 0 1 47 1059 Z"
        fill="none" stroke="var(--frame-line)" stroke-width="2"/>

  <text class="podcast-title" x="600" y="520" text-anchor="middle">QUIET HARBOR</text>
  <text class="podcast-title" x="600" y="636" text-anchor="middle">LEDGER HOUR</text>

  <ellipse class="title-floor-shadow" cx="600" cy="795" rx="250" ry="26" fill="url(#floor-shadow)"/>

  <text class="subtitle" x="101" y="915" textLength="998" lengthAdjust="spacingAndGlyphs">CREATIVE INTERNET INCOME STRATEGIES</text>
  <rect class="subtitle-rule" x="101" y="931" width="998" height="2" fill="var(--subtitle-rule)"/>
</svg>
</body>
</html>
```